Tidewell Ventures Wordpress / Web Design - Agile Coaching

UPDATE: PLEASE USE MORE ICONS/GRAPHICS THEN PHOTOS. THANK YOU!

We need a web design for a new company called Tidewell Ventures. We do agile coaching, consulting, training and facilitation for medium to large enterprise, most just starting their agile journey. We want to be professional, but light and whimsical. We have started loading content onto the www.tidewellventures.example website, using the Marlow Theme (real flexibility!)

We have a logo, and I really liked it, although if needed the colors can be adjusted depending on the design. I would advice sticking with the logo and its colors unless they become problematic or you have a fantastic idea.

I really like the colors found on stickum slips, and use stickum slips in all my coaching and training. I want to warn though, I don't want the whole site to be splashes of color, but I would like some pop of color, and you could use the stickum slip colors and the idea of stickum slips for icon designs or sparingly for emphasis, but keep the design simple with lots of white space. I'm inspired by this template from Pattern Bazaar and use the power point in the 2nd attached file...this may inspire you.

I have another contest running right now, if you want to check that out as well, but it isn't necessary. Contest is titled "Tidewell Ventures: Software Development Consultancy Needs a Business Card Design"

Target Market(s)

medium to large software companies needing to improve the speed, quality and value of their software delivery

Industry/Entity Type

Information Technology

Number of Pages Required

3 page

Font styles to use
Sans Serif

Requirements
Must have
• Simple, easy to use, easy navigation, space!
• content on my front page is accurate so should be included www.tidewellventures.example
• 2nd page you can look at is http://www.tidewellventures.example/inspiration/
• 3rd page you can look at is http://www.tidewellventures.example/reference-list/ (about twice as many links are going to be added in next two days!)
Nice to have
• take a look at any other page on the site. if something is password protected, use the word "password" as the password.
• Update: I like less pictures, more graphics.
Should not have
• too crowded. hard to navigate. childish graphics. too boring and corporate. :)

```html
<!DOCTYPE html>
<html lang="en">
<head>
<meta charset="utf-8">
<title>Tidewell Ventures</title>
<link href="https://fonts.googleapis.com/css2?family=Open+Sans:wght@400;600;700&display=swap" rel="stylesheet">
<style>
:root{
  --brand:#1f6fb2;
  --brand-dark:#17486f;
  --navy:#1d3f63;
  --navy-deep:#142f4c;
  --ink:#333;
  --muted:#8a8a8a;
  --line:#e4e4e4;
  --soft:#f6f6f6;
  --pink:#e8304f;
  --purple:#8a4fb8;
  --green:#7cbf2f;
  --sky:#2f8fd8;
}
*{box-sizing:border-box;margin:0;padding:0}
html,body{width:1200px;height:2380px;overflow:hidden;background:#fff}
body{font-family:"Open Sans",Arial,sans-serif;color:var(--ink);position:relative}
.wrap{width:1000px;margin:0 auto;position:relative}

/* header */
.site-header{height:108px;border-bottom:1px solid var(--line)}
.site-header .wrap{display:flex;align-items:center;justify-content:space-between;height:108px}
.brand{display:flex;align-items:center;gap:12px;font-weight:700;font-size:24px;color:var(--brand)}
.brand-dot{width:40px;height:40px;border-radius:50%;background:var(--brand)}
.main-nav{display:flex;gap:0}
.main-nav a{font-size:11px;font-weight:600;color:#555;text-decoration:none;padding:0 16px;height:108px;line-height:108px;border-left:1px solid var(--line);letter-spacing:.5px}
.main-nav a.active{color:var(--brand)}
.main-nav a:last-child{border-right:1px solid var(--line)}

/* hero */
.hero{height:528px;position:relative;background:linear-gradient(120deg,#6d6f73 0%,#b9bcc0 35%,#dfe3e7 60%,#c5cfd8 100%)}
.hero-title{position:absolute;left:600px;top:170px;font-size:44px;font-weight:700;color:var(--navy);letter-spacing:1px}
.hero-sub{position:absolute;left:604px;top:232px;font-size:24px;color:var(--navy)}
.hero-arrow{position:absolute;top:244px;width:40px;height:40px;border-radius:50%;background:rgba(60,60,60,.55)}
.hero-arrow.prev{left:30px}.hero-arrow.next{right:30px}
.hero-arrow svg{width:40px;height:40px}

/* welcome */
.welcome{height:164px;text-align:center;padding-top:36px}
.welcome h1{font-size:30px;font-weight:400;color:#333;margin-bottom:16px}
.welcome p{width:920px;margin:0 auto;font-size:12px;line-height:20px;color:var(--muted)}

/* services */
.services{height:370px;border-top:1px solid var(--line);border-bottom:1px solid var(--line);background:var(--soft)}
.services .wrap{display:flex;justify-content:space-between;padding-top:70px}
.service{width:220px;text-align:center}
.service svg{width:100px;height:100px}
.service h3{font-size:14px;font-weight:700;margin:22px 0 8px;letter-spacing:.5px}
.service p{font-size:11px;line-height:17px;color:var(--muted)}

/* blog */
.blog{height:500px;padding-top:50px}
.section-title{text-align:center;font-size:20px;font-weight:400;letter-spacing:1px;margin-bottom:26px;position:relative}
.section-title span{background:#fff;padding:0 18px;position:relative}
.section-title:before{content:"";position:absolute;left:0;right:0;top:50%;border-top:1px solid var(--line)}
.blog-grid{display:flex;justify-content:space-between}
.post{width:244px;border:1px solid var(--line);height:380px;background:#fff}
.post-media{height:170px}
.post-body{padding:20px 14px 0;height:158px}
.post h4{font-size:14px;font-weight:600;margin-bottom:10px}
.post p{font-size:11px;line-height:17px;color:var(--muted)}
.post-meta{border-top:1px solid var(--line);height:50px;display:flex;align-items:center;justify-content:space-between;padding:0 14px;font-size:11px;color:var(--muted)}
.post-meta b{width:8px;height:8px;border-radius:50%;background:#ccc}

/* extras row */
.extras{height:340px}
.extras .wrap{display:flex;justify-content:space-between;padding-top:26px}
.col-inspire{width:280px}
.col-title{font-size:13px;font-weight:700;letter-spacing:.5px;margin-bottom:16px}
.col-inspire .col-title{color:var(--brand)}
.inspire-media{height:186px}
.col-testi{width:340px;padding-top:40px}
.col-testi .col-title{text-align:center;font-weight:400;font-size:14px}
.quote{border:1px solid var(--line);padding:16px 18px;font-size:11px;line-height:17px;color:var(--muted);position:relative}
.author{display:flex;align-items:center;gap:12px;margin-top:22px;padding-left:20px;font-size:12px}
.avatar{width:52px;height:52px;border-radius:50%;background:#b9b2a8}
.author b{font-weight:600}.author i{font-style:normal;color:var(--muted)}
.col-feed{width:300px;border:1px solid var(--line);height:262px;background:var(--soft)}
.feed-head{display:flex;justify-content:space-between;align-items:center;padding:12px 14px;border-bottom:1px solid var(--line);background:#fff;font-size:12px;font-weight:600}
.follow{font-size:10px;border:1px solid #ccc;border-radius:3px;padding:2px 8px;color:#555;font-weight:400}
.tweet{display:flex;gap:10px;padding:16px 14px;border-bottom:1px solid var(--line);background:#fff;margin:10px;font-size:10px;line-height:15px;color:var(--muted)}
.tweet-avatar{width:30px;height:30px;flex:none;background:#9aa4ad}
.tweet b{color:#333;font-weight:600}

/* footer */
.site-footer{position:absolute;left:0;top:2010px;width:1200px;height:320px;background:var(--navy);color:#d6e0ea}
.site-footer .wrap{display:flex;justify-content:space-between;padding-top:36px}
.fcol{width:220px;font-size:11px;line-height:18px}
.fcol h5{font-size:14px;font-weight:400;letter-spacing:.5px;color:#fff;margin-bottom:14px}
.socials{display:flex;gap:6px;margin-top:14px}
.socials span{width:18px;height:18px;background:#d6e0ea}
.signup{display:flex;margin-top:16px}
.signup span{background:#fff;color:#999;height:32px;line-height:32px;padding:0 10px;width:150px}
.signup b{background:var(--navy-deep);color:#fff;font-weight:400;height:32px;line-height:32px;padding:0 12px;border:1px solid #5d7894}
.links{list-style:none}
.links li{padding-left:12px;position:relative}
.links li:before{content:"";position:absolute;left:0;top:7px;width:4px;height:4px;border-radius:50%;background:#d6e0ea}
.contact-line{display:flex;gap:8px;align-items:flex-start;margin-bottom:6px}
.contact-line svg{width:14px;height:14px;flex:none;margin-top:2px}
.legal{position:absolute;left:0;top:2330px;width:1200px;height:50px;background:var(--navy-deep);color:#9fb3c7;font-size:10px;text-align:center;line-height:50px}
</style>
</head>
<body>

<header class="site-header">
  <div class="wrap">
    <div class="brand"><span class="brand-dot"></span>Tidewell Ventures</div>
    <nav class="main-nav">
      <a class="active">HOME</a><a>ABOUT US</a><a>OUR SERVICES</a><a>INSPIRATION</a><a>AVAILABILITY</a><a>BLOG</a><a>CONTACT US</a>
    </nav>
  </div>
</header>

<section class="hero" role="img" aria-label="Photo of a businessman holding a magnifying glass over a glowing globe above a city skyline">
  <div class="hero-title">TIDEWELL</div>
  <div class="hero-sub">Ventures</div>
  <div class="hero-arrow prev"><svg viewBox="0 0 40 40"><path d="M23 13l-7 7 7 7" fill="none" stroke="#fff" stroke-width="2.5"/></svg></div>
  <div class="hero-arrow next"><svg viewBox="0 0 40 40"><path d="M17 13l7 7-7 7" fill="none" stroke="#fff" stroke-width="2.5"/></svg></div>
</section>

<section class="welcome">
  <h1>Welcome To Tidewell Ventures</h1>
  <p>Lorem ipsum dolor sit amet, consectetur adipiscing elit, sed do eiusmod tempor incididunt ut labore et dolore magna aliqua. Ut enim ad minim veniam, quis nostrud exercitation ullamco laboris nisi ut aliquip ex ea commodo consequat. Duis aute irure dolor in reprehenderit in voluptate velit esse cillum dolore eu fugiat nulla pariatur. Excepteur sint occaecat cupidatat non proident, sunt in culpa qui officia deserunt mollit anim id est laborum.</p>
</section>

<section class="services">
  <div class="wrap">
    <div class="service">
      <svg viewBox="0 0 100 100"><circle cx="50" cy="50" r="44" fill="#fff" stroke="#ddd" stroke-width="6"/><path d="M50 6a44 44 0 0 1 38 22" fill="none" stroke="var(--pink)" stroke-width="6"/><circle cx="42" cy="42" r="6" fill="var(--pink)"/><circle cx="60" cy="42" r="6" fill="var(--pink)"/><path d="M30 64a12 10 0 0 1 24 0zM48 64a12 10 0 0 1 24 0z" fill="var(--pink)"/></svg>
      <h3>COACHING</h3>
      <p>Lorem ipsum dolor sit amet, consectetur adipiscing elit, sed do eiusmod tempor incididunt ut labore et dolore.</p>
    </div>
    <div class="service">
      <svg viewBox="0 0 100 100"><circle cx="50" cy="50" r="44" fill="#fff" stroke="#ddd" stroke-width="6"/><path d="M50 6a44 44 0 0 0 -40 26" fill="none" stroke="var(--purple)" stroke-width="6"/><circle cx="50" cy="44" r="12" fill="none" stroke="var(--purple)" stroke-width="3"/><rect x="44" y="58" width="12" height="8" fill="var(--purple)"/></svg>
      <h3>CONSULTING</h3>
      <p>Lorem ipsum dolor sit amet, consectetur adipiscing elit, sed do eiusmod tempor incididunt ut labore et dolore.</p>
    </div>
    <div class="service">
      <svg viewBox="0 0 100 100"><circle cx="50" cy="50" r="44" fill="#fff" stroke="#ddd" stroke-width="6"/><path d="M50 6a44 44 0 0 1 44 44" fill="none" stroke="var(--green)" stroke-width="6"/><rect x="36" y="36" width="14" height="14" fill="var(--green)"/><rect x="52" y="36" width="14" height="14" fill="#a6d36a"/><rect x="36" y="52" width="14" height="14" fill="#a6d36a"/><rect x="52" y="52" width="14" height="14" fill="var(--green)"/></svg>
      <h3>TRAINING</h3>
      <p>Lorem ipsum dolor sit amet, consectetur adipiscing elit, sed do eiusmod tempor incididunt ut labore et dolore.</p>
    </div>
    <div class="service">
      <svg viewBox="0 0 100 100"><circle cx="50" cy="50" r="44" fill="#fff" stroke="#ddd" stroke-width="6"/><path d="M50 6a44 44 0 0 1 40 26" fill="none" stroke="var(--sky)" stroke-width="6"/><circle cx="50" cy="52" r="15" fill="var(--sky)"/><path d="M53 34v15h15a15 15 0 0 0 -15 -15z" fill="#7dbbea"/></svg>
      <h3>FACILIATION</h3>
      <p>Lorem ipsum dolor sit amet, consectetur adipiscing elit, sed do eiusmod tempor incididunt ut labore et dolore.</p>
    </div>
  </div>
</section>

<section class="blog">
  <div class="wrap">
    <h2 class="section-title"><span>RECENT BLOG</span></h2>
    <div class="blog-grid">
      <article class="post">
        <div class="post-media" role="img" aria-label="Photo of a trainer presenting to a small group" style="background:linear-gradient(135deg,#d9d4cc,#8c8f96)"></div>
        <div class="post-body"><h4>Sed docendi copiosae</h4><p>Lorem ipsum dolor sit amet, consectetur adipiscing elit, sed do eiusmod tempor incididunt ut labore.</p></div>
        <div class="post-meta">July 25, 2015<b></b></div>
      </article>
      <article class="post">
        <div class="post-media" role="img" aria-label="Photo of hands working on laptops around a wooden table" style="background:linear-gradient(135deg,#7a5a3e,#c9b9a3)"></div>
        <div class="post-body"><h4>Sed docendi copiosae</h4><p>Lorem ipsum dolor sit amet, consectetur adipiscing elit, sed do eiusmod tempor incididunt ut labore.</p></div>
        <div class="post-meta">July 25, 2015<b></b></div>
      </article>
      <article class="post">
        <div class="post-media" role="img" aria-label="Photo of a team putting hands together in a huddle" style="background:linear-gradient(135deg,#2a2f3a,#6b7a94)"></div>
        <div class="post-body"><h4>Sed docendi copiosae</h4><p>Lorem ipsum dolor sit amet, consectetur adipiscing elit, sed do eiusmod tempor incididunt ut labore.</p></div>
        <div class="post-meta">July 25, 2015<b></b></div>
      </article>
      <article class="post">
        <div class="post-media" role="img" aria-label="Photo of business people holding umbrellas under a stormy sky" style="background:linear-gradient(180deg,#3a6ea8,#1e2f44)"></div>
        <div class="post-body"><h4>Sed docendi copiosae</h4><p>Lorem ipsum dolor sit amet, consectetur adipiscing elit, sed do eiusmod tempor incididunt ut labore.</p></div>
        <div class="post-meta">July 25, 2015<b></b></div>
      </article>
    </div>
  </div>
</section>

<section class="extras">
  <div class="wrap">
    <div class="col-inspire">
      <h3 class="col-title">INSPIRATION</h3>
      <div class="inspire-media" role="img" aria-label="Photo of a businessman juggling many tasks against a pale sky" style="background:linear-gradient(135deg,#cfe0ee,#8fb1cf)"></div>
    </div>
    <div class="col-testi">
      <h3 class="col-title">TESTIMONIALS</h3>
      <div class="quote">Lorem ipsum dolor sit amet, consectetur adipiscing elit, sed do eiusmod tempor incididunt ut labore et dolore magna aliqua. Ut enim ad minim veniam, quis nostrud exercitation ullamco laboris.</div>
      <div class="author"><span class="avatar" role="img" aria-label="Client portrait"></span><span><b>John Doe</b> <i>- Manager</i></span></div>
    </div>
    <div class="col-feed">
      <div class="feed-head">Chirpline Updates<span class="follow">Follow</span></div>
      <div class="tweet"><span class="tweet-avatar"></span><span><b>Nora Pellam</b> @tidewell<br>Lorem ipsum dolor sit amet consectetur adipiscing elit sed do.</span></div>
      <div class="tweet"><span class="tweet-avatar"></span><span><b>Nora Pellam</b> @tidewell<br>Lorem ipsum dolor sit amet consectetur adipiscing elit sed do.</span></div>
    </div>
  </div>
</section>

<footer class="site-footer">
  <div class="wrap">
    <div class="fcol">
      <h5>ABOUT US</h5>
      <p>Lorem ipsum dolor sit amet, consectetur adipiscing elit, sed do eiusmod tempor incididunt ut labore et dolore magna aliqua.</p>
      <div class="socials"><span></span><span></span><span></span><span></span></div>
    </div>
    <div class="fcol" style="width:260px">
      <h5>JOIN OUR NEWSLETTER</h5>
      <p>Sign up for our latest news and updates, delivered straight to your inbox.</p>
      <div class="signup"><span>Your Email</span><b>Subscribe</b></div>
    </div>
    <div class="fcol" style="width:150px">
      <h5>INFORMATION</h5>
      <ul class="links"><li>Home</li><li>Services</li><li>Inspiration</li><li>Availability</li><li>Blog</li><li>Contact</li></ul>
    </div>
    <div class="fcol">
      <h5>CONTACT US</h5>
      <div class="contact-line"><svg viewBox="0 0 14 14"><path d="M7 1a4 4 0 0 1 4 4c0 3-4 8-4 8S3 8 3 5a4 4 0 0 1 4-4z" fill="#d6e0ea"/></svg><span>214 Harbor Lane, Fairport</span></div>
      <div class="contact-line"><svg viewBox="0 0 14 14"><path d="M3 1h3l1 3-2 1a8 8 0 0 0 4 4l1-2 3 1v3a1 1 0 0 1-1 1A11 11 0 0 1 2 2a1 1 0 0 1 1-1z" fill="#d6e0ea"/></svg><span>+1 555 014 8830</span></div>
      <div class="contact-line"><svg viewBox="0 0 14 14"><rect x="1" y="3" width="12" height="8" fill="none" stroke="#d6e0ea"/><path d="M1 3l6 5 6-5" fill="none" stroke="#d6e0ea"/></svg><span>hello@tidewellventures.example</span></div>
    </div>
  </div>
</footer>
<div class="legal">© Copyright 2015, Tidewell Ventures LLC. All Rights Reserved.</div>

</body>
</html>
```